Business Card Design for Varnok Facility Services

We are looking for a Business Card Design for the Company "Varnok Facility Services."
Front side:
- Company Logo (small)
- Company Name, address, pohone, website and personal data.
- white background, for text e.g. company colors (blue or green like in the logo)
Please use following data:
Company data:
Varnok Facility Services Tulbrecht
Kirchmattweg 12
6331 Cham
www.varnok-fs.ch
Person data:
Ruben Tulbrecht
Geschäftsführer
+41 76 519 84 60
info@varnok-fs.ch
Back side:
could be colored in blue or green
please use a big logo sing and some smaller icons to say what is all beeing offered in facility services, like cleaning, maintenance cleaning
industrial cleaning, caretaking, gardening, disposal. There is no need for everyone of the icons if there are similar or an icon is standing for more of them.
Cleaning Service
colors to use:
blue: HEX 246BB0
green: HEX 52B33E

```html
<!DOCTYPE html>
<html lang="de">
<head>
<meta charset="utf-8">
<title>Varnok Facility Services – Business Card</title>
<link rel="stylesheet" href="https://fonts.googleapis.com/css2?family=Arimo:wght@400;700&display=swap">
<style>
  :root {
    --brand-blue: #246BB0;
    --brand-green: #52B33E;
    --paper: #ffffff;
    --backdrop: #2b2b2d;
    --card-w: 600px;
    --card-h: 345px;
  }
  * { box-sizing: border-box; margin: 0; padding: 0; }
  html, body { width: 1200px; height: 880px; overflow: hidden; }
  body {
    background: var(--backdrop);
    font-family: "Arimo", Arial, sans-serif;
    position: relative;
  }
  .card {
    position: absolute;
    width: var(--card-w);
    height: var(--card-h);
    border-radius: 22px;
    overflow: hidden;
  }
  .card--back { left: 120px; top: 70px; background: var(--brand-blue); color: var(--paper); }
  .card--front { left: 480px; top: 465px; background: var(--paper); }

  /* brand lockup */
  .brand { display: flex; align-items: center; gap: 12px; position: absolute; }
  .brand__dot { width: 22px; height: 22px; border-radius: 50%; flex: none; }
  .brand__name { font-weight: 700; line-height: 1.05; }

  .card--back .brand { left: 0; right: 0; top: 96px; justify-content: center; }
  .card--back .brand__dot { background: var(--paper); width: 30px; height: 30px; }
  .card--back .brand__name { font-size: 40px; color: var(--paper); }

  .services {
    position: absolute; left: 0; right: 0; top: 200px;
    text-align: center; font-size: 13.5px; line-height: 1.6;
  }

  /* front */
  .card__waves { position: absolute; inset: 0; }
  .card--front .brand { left: 48px; top: 88px; }
  .card--front .brand__dot { background: var(--brand-green); }
  .card--front .brand__name { font-size: 27px; color: var(--brand-blue); width: 200px; }

  .holder { position: absolute; right: 34px; top: 26px; text-align: right; }
  .holder__name { color: var(--brand-blue); font-weight: 700; font-size: 17px; letter-spacing: .3px; }
  .holder__role { color: var(--brand-green); font-size: 13px; margin-top: 2px; }

  .contact {
    position: absolute; right: 34px; top: 126px; text-align: right;
    color: var(--paper); font-size: 12.5px; line-height: 1.55;
  }
  .contact__line { display: flex; justify-content: flex-end; align-items: center; gap: 8px; }
  .contact__icon { width: 16px; height: 16px; flex: none; }
  .contact__company { font-weight: 700; margin-top: 10px; }
</style>
</head>
<body>

<section class="card card--back" aria-label="Business card, back side">
  <div class="brand">
    <span class="brand__dot"></span>
    <span class="brand__name">Varnok Facility Services</span>
  </div>
  <p class="services">
    facility services | like cleaning | maintenance cleaning | industrial cleaning<br>
    caretaking | gardening | disposal
  </p>
</section>

<section class="card card--front" aria-label="Business card, front side">
  <svg class="card__waves" viewBox="0 0 600 345" width="600" height="345" aria-hidden="true">
    <defs>
      <linearGradient id="green-sweep" x1="0" y1="1" x2="1" y2="0">
        <stop offset="0" stop-color="#8bcf4a"/>
        <stop offset="1" stop-color="#52B33E"/>
      </linearGradient>
    </defs>
    <path d="M0,305 C150,300 250,300 300,225 C360,125 420,72 600,62 L600,345 L0,345 Z" fill="#246BB0"/>
    <path d="M120,345 C250,320 300,280 335,205 C375,120 430,80 600,70" fill="none" stroke="#ffffff" stroke-width="5"/>
    <path d="M0,262 C160,262 250,250 300,150 C250,240 170,282 0,290 Z" fill="url(#green-sweep)"/>
    <path d="M0,292 C170,292 260,272 305,205" fill="none" stroke="#ffffff" stroke-width="4"/>
  </svg>

  <div class="brand">
    <span class="brand__dot"></span>
    <span class="brand__name">Varnok Facility Services</span>
  </div>

  <div class="holder">
    <p class="holder__name">RUBEN TULBRECHT</p>
    <p class="holder__role">Geschäftsführer</p>
  </div>

  <div class="contact">
    <p class="contact__line">+41 76 519 84 60
      <svg class="contact__icon" viewBox="0 0 16 16" aria-hidden="true"><circle cx="8" cy="8" r="7.2" fill="none" stroke="#fff" stroke-width="1.3"/><path d="M5.3 4.2l1.4 1.6-.8 1.1c.5 1.1 1.3 1.9 2.3 2.4l1.1-.8 1.6 1.4-.9 1.4C7.4 11.1 4.8 8.6 4 5.1z" fill="#fff"/></svg>
    </p>
    <p class="contact__line">info@varnok-fs.ch
      <svg class="contact__icon" viewBox="0 0 16 16" aria-hidden="true"><circle cx="8" cy="8" r="7.2" fill="none" stroke="#fff" stroke-width="1.3"/><rect x="4.2" y="5.3" width="7.6" height="5.4" fill="none" stroke="#fff" stroke-width="1"/><path d="M4.2 5.3L8 8.4l3.8-3.1" fill="none" stroke="#fff" stroke-width="1"/></svg>
    </p>
    <p class="contact__company">Varnok Facility Services Tulbrecht</p>
    <p>Kirchmattweg 12</p>
    <p>6331 Cham</p>
    <p>www.varnok-fs.ch</p>
  </div>
</section>

</body>
</html>
```